HVAC Technical Manual Covers for Duct Design, Load Calculation and Equipment Selection

I work for an HVAC trade association that publishes technical manuals. We have a series of books that need new covers since there have been many changes.

I'd like the books to have a similar style to each other (like the current Guide T and P, see below). Here is a listing of all our current manuals https://www.brevona.org/standards/technical-manuals. We plan on updating more in the future, like H, , N and ZR. So I'd like a design that we can continue on.

The 3 covers I need are
1. Guide Q Residential Load Calculation
https://www.brevona.org/standards/technical-manuals/manual-j
2. Guide P® - Residential Duct Systems
https://www.brevona.org/standards/technical-manuals/manual-d
3. Guide T® - Residential Equipment Selection
https://www.brevona.org/standards/technical-manuals/manual-s

I included our logos and style guide as a resource. But I'm open to all images and colors. The audience is primarily engineers, software developers, code officials and HVAC technicians. These 3 manuals are aimed at residential (single-family homes/townhomes) in the United States.

Target Market(s)

The audience is primarily engineers, software developers, code officials and HVAC technicians.

Industry/Entity Type

HVACR, Air Conditioning

Font styles to use
Sans Serif

Requirements
Must have
• BRVO Logo, manual letter and full title. Single Family or townhome images
Should not have
• commercial buildings, mini splits, hardhats

```html
<!DOCTYPE html>
<html lang="en">
<head>
<meta charset="utf-8">
<title>Guide Q – Residential Load Calculation</title>
<link rel="stylesheet" href="https://fonts.googleapis.com/css2?family=Anton&family=Roboto+Condensed:wght@700&display=swap">
<style>
  :root {
    --backdrop: #878a7c;
    --paper: #f2f2f3;
    --brand-blue: #1f6fb2;
    --deep-blue: #0b4f91;
    --ink: #1c1c1e;
    --white: #ffffff;
    --photo-light: #c9d2dc;
    --photo-mid: #7f93a9;
    --photo-dark: #3d4f66;
  }
  * { box-sizing: border-box; margin: 0; padding: 0; }
  html, body {
    width: 1200px;
    height: 960px;
    overflow: hidden;
    background: var(--backdrop);
  }
  .cover {
    position: absolute;
    left: 330px;
    top: 120px;
    width: 540px;
    height: 720px;
    background: var(--paper);
    overflow: hidden;
  }
  .cover-spine {
    position: absolute;
    left: 0; top: 0;
    width: 14px; height: 100%;
    background: var(--deep-blue);
    z-index: 5;
  }
  .cover-photo {
    position: absolute;
    left: 0; top: 0;
    width: 100%; height: 280px;
    background: linear-gradient(125deg, var(--photo-light) 0%, var(--photo-mid) 45%, var(--photo-dark) 100%);
  }
  .manual-letter {
    position: absolute;
    left: 140px;
    top: 30px;
    width: 230px;
    font-family: "Anton", sans-serif;
    font-size: 380px;
    line-height: 1;
    text-align: center;
    color: var(--ink);
    z-index: 2;
  }
  .manual-label {
    position: absolute;
    left: 92px;
    top: 218px;
    padding: 4px 12px 2px;
    background: var(--brand-blue);
    border: 2px solid var(--white);
    font-family: "Roboto Condensed", sans-serif;
    font-weight: 700;
    font-size: 34px;
    letter-spacing: 1px;
    color: var(--white);
    z-index: 3;
  }
  .brand {
    position: absolute;
    left: 392px;
    top: 296px;
    display: flex;
    align-items: center;
    gap: 8px;
    font-family: "Roboto Condensed", sans-serif;
    font-weight: 700;
    font-size: 34px;
    line-height: 1;
    color: var(--brand-blue);
    z-index: 4;
  }
  .brand-mark {
    width: 14px; height: 14px;
    background: var(--brand-blue);
  }
  .accent-block {
    position: absolute;
    left: 370px;
    top: 420px;
    width: 170px;
    height: 230px;
    background: linear-gradient(100deg, var(--brand-blue), var(--deep-blue));
    z-index: 1;
  }
  .cover-title {
    position: absolute;
    left: 44px;
    top: 488px;
    font-family: "Anton", sans-serif;
    font-weight: 400;
    font-size: 46px;
    line-height: 1.08;
    letter-spacing: 1px;
    color: var(--brand-blue);
    text-transform: uppercase;
  }
  .title-rule {
    position: absolute;
    left: 44px;
    top: 664px;
    width: 176px;
    height: 20px;
    background: var(--brand-blue);
  }
</style>
</head>
<body>
  <main class="cover">
    <div class="cover-spine"></div>
    <div class="cover-photo" role="img" aria-label="Photo of an engineer at a desk reviewing documents and pointing at a tablet with a laptop nearby"></div>
    <div class="manual-letter" aria-hidden="true">Q</div>
    <div class="manual-label">GUIDE</div>
    <div class="brand"><span class="brand-mark"></span>BRVO</div>
    <div class="accent-block"></div>
    <h1 class="cover-title">Residential<br>Load<br>Calculation</h1>
    <div class="title-rule"></div>
  </main>
</body>
</html>
```